Pelin Thai Massage Double Sided Flyer Luxury

I require a double sided flyer
we are a Thai Massage Spa
Would like gold, deep purple and bronze colours
Something eye catching and looks professional

```html
<!DOCTYPE html>
<html lang="en">
<head>
<meta charset="utf-8">
<title>Pelin Thai Massage – Deep Tissue Flyer</title>
<link rel="stylesheet" href="https://fonts.googleapis.com/css2?family=Marcellus&family=Playball&family=Kreon:wght@600;700&family=Signika:wght@300;600&family=Open+Sans:wght@400;600&family=Libre+Baskerville:wght@700&display=swap">
<style>
  :root {
    --purple: #5f2589;
    --purple-deep: #4a1566;
    --purple-dark: #2f1048;
    --purple-light: #8250a8;
    --violet: #4f2f8f;
    --badge: #4b2a8c;
    --white: #ffffff;
    --text-soft: #eef1f4;
  }
  * { margin: 0; padding: 0; box-sizing: border-box; }
  html, body { width: 875px; height: 1200px; overflow: hidden; background: var(--white); }
  .flyer { position: relative; width: 875px; height: 1200px; overflow: hidden; color: var(--white); font-family: "Open Sans", sans-serif; }
  .backdrop { position: absolute; inset: 0; }

  .brand { position: absolute; left: 648px; top: 18px; width: 160px; text-align: center; color: var(--purple-light); font-family: "Signika", sans-serif; font-weight: 300; font-size: 13px; }
  .brand-mark { width: 54px; height: 54px; margin: 0 auto 8px; border: 3px solid var(--purple-light); border-radius: 50%; }

  .headline { position: absolute; left: 0; width: 875px; top: 538px; text-align: center; font-family: "Marcellus", serif; font-size: 64px; line-height: 1; color: var(--text-soft); letter-spacing: 0.5px; }
  .headline-rule { position: absolute; left: 185px; top: 609px; width: 520px; height: 2px; background: linear-gradient(90deg, transparent, var(--text-soft) 10%, var(--text-soft) 90%, transparent); }
  .tagline { position: absolute; left: 84px; top: 616px; width: 760px; font-family: "Playball", cursive; font-size: 33px; line-height: 37px; color: var(--text-soft); }

  .treatment { position: absolute; top: 756px; }
  .treatment-photo { position: absolute; top: 0; width: 170px; height: 170px; border-radius: 50%; border: 5px solid var(--white); }
  .price-badge { position: absolute; width: 58px; height: 58px; border-radius: 50%; background: var(--badge); border: 4px solid var(--white); display: flex; align-items: center; justify-content: center; font-family: "Kreon", serif; font-weight: 600; font-size: 22px; }
  .treatment-price { position: absolute; white-space: nowrap; font-family: "Kreon", serif; font-weight: 700; font-size: 33px; line-height: 1; }
  .treatment-note { position: absolute; white-space: nowrap; font-size: 11.5px; line-height: 13px; }
  .treatment-note strong { font-weight: 600; font-size: 11px; }

  .name-pill { position: absolute; left: 252px; top: 1003px; width: 354px; height: 47px; border-radius: 24px; background: var(--white); color: var(--violet); font-family: "Signika", sans-serif; font-weight: 600; font-size: 36px; line-height: 47px; text-align: center; }

  .contact { position: absolute; font-family: "Signika", sans-serif; font-weight: 300; font-size: 28px; line-height: 31px; display: flex; align-items: flex-start; gap: 6px; }
  .contact svg { flex: none; margin-top: 1px; }
  .contact-address { left: 94px; top: 1056px; }
  .contact-phone { left: 520px; top: 1057px; }
  .contact-divider { position: absolute; left: 440px; top: 1062px; width: 1px; height: 56px; background: var(--white); }

  .web-pill { position: absolute; left: 167px; top: 1129px; width: 548px; height: 34px; border-radius: 17px; background: var(--white); color: var(--violet); font-family: "Libre Baskerville", serif; font-weight: 700; font-size: 13px; letter-spacing: 8.2px; line-height: 34px; text-align: center; }
</style>
</head>
<body>
<main class="flyer">
  <svg class="backdrop" viewBox="0 0 875 1200" width="875" height="1200" aria-hidden="false">
    <defs>
      <linearGradient id="photoTones" x1="0" y1="0" x2="1" y2="1">
        <stop offset="0" stop-color="#d9c6b4"/>
        <stop offset="0.35" stop-color="#8a5a44"/>
        <stop offset="0.6" stop-color="#d49a78"/>
        <stop offset="1" stop-color="#b07c5a"/>
      </linearGradient>
      <linearGradient id="lowerPurple" x1="0" y1="0" x2="1" y2="1">
        <stop offset="0" stop-color="#682e96"/>
        <stop offset="1" stop-color="#4a1462"/>
      </linearGradient>
      <linearGradient id="topBand" x1="0" y1="0" x2="0" y2="1">
        <stop offset="0" stop-color="#8a55ae"/>
        <stop offset="1" stop-color="#541c7a"/>
      </linearGradient>
    </defs>
    <rect x="0" y="0" width="875" height="560" fill="url(#photoTones)" role="img" aria-label="Photograph of a woman relaxing on a massage table, wrapped in a brown towel, as a therapist massages her shoulder"/>
    <path d="M0,0 L875,0 L875,92 C720,120 600,110 480,60 C330,-5 150,-5 0,45 Z" fill="var(--white)"/>
    <path d="M0,45 C150,-5 330,-5 480,60 C600,110 720,120 875,92 L875,176 C850,185 820,193 770,195 C660,200 560,130 420,60 C300,15 150,25 0,75 Z" fill="url(#topBand)"/>
    <path d="M0,258 C100,255 200,300 272,346 C190,310 100,285 0,284 Z" fill="var(--violet)"/>
    <path d="M875,368 C800,440 700,490 540,505 C700,515 800,490 875,478 Z" fill="var(--violet)"/>
    <path d="M0,298 C190,290 330,370 510,455 C660,522 780,515 875,485 L875,1200 L0,1200 Z" fill="var(--purple-dark)"/>
    <path d="M0,340 C190,330 330,400 520,475 C660,525 780,522 875,510 L875,1200 L0,1200 Z" fill="var(--white)"/>
    <path d="M0,364 C190,352 330,420 520,492 C660,540 780,540 875,530 L875,1200 L0,1200 Z" fill="url(#lowerPurple)"/>
  </svg>

  <div class="brand">
    <div class="brand-mark"></div>
    Pelin Thai Massage
  </div>

  <h1 class="headline">DEEP TISSUE MASSAGE</h1>
  <div class="headline-rule"></div>
  <p class="tagline">Restore balance. Revive your senses.<br>Discover all the ways Pelin Thai Massage can<br>breathe new life into your body and soul</p>

  <section class="treatment" style="left:37px">
    <div class="treatment-photo" style="left:55px; background: radial-gradient(circle at 40% 60%, #7a6a66, #d7dde3 60%, #c9ced4);" role="img" aria-label="Photo of oil being poured from a small bowl into a hand"></div>
    <div class="price-badge" style="left:167px; top:116px">£45</div>
    <div class="treatment-price" style="left:48px; top:178px">60 minutes £45</div>
    <div class="treatment-note" style="left:48px; top:215px">Oil massage personalised, light to firm pressure</div>
  </section>

  <section class="treatment" style="left:332px">
    <div class="treatment-photo" style="left:22px; background: radial-gradient(circle at 65% 45%, #f7d98a, #a27a4c 45%, #4c3a2c 85%);" role="img" aria-label="Photo of rolled towels beside lit candles"></div>
    <div class="price-badge" style="left:128px; top:128px; width:50px; height:50px; font-size:19px">£55</div>
    <div class="treatment-price" style="left:15px; top:178px">90 minutes £55</div>
    <div class="treatment-note" style="left:15px; top:212px">Oil massage, medium to firm pressure<br><strong>THAI FLOOR TRADITIONAL MASSAGE</strong></div>
  </section>

  <section class="treatment" style="left:595px">
    <div class="treatment-photo" style="left:7px; background: radial-gradient(circle at 50% 50%, #c08866, #6e4a3c 55%, #2f5e78 90%);" role="img" aria-label="Photo of a client receiving a neck and shoulder massage"></div>
    <div class="price-badge" style="left:127px; top:116px">£45</div>
    <div class="treatment-price" style="left:0; top:174px">60 minutes £45</div>
    <div class="treatment-note" style="left:0; top:209px">Dry massage, medium to firm pressure<br>applying stretching technique</div>
  </section>

  <div class="name-pill">Pelin Thai massage</div>

  <div class="contact contact-address">
    <svg width="30" height="30" viewBox="0 0 30 30" aria-hidden="true"><circle cx="15" cy="15" r="15" fill="#fff"/><path d="M15 7a6 6 0 0 0-6 6c0 4.5 6 10 6 10s6-5.5 6-10a6 6 0 0 0-6-6z" fill="#5f2589"/><circle cx="15" cy="13" r="2.3" fill="#fff"/></svg>
    <span>42 Orchard Row, Leeds<br>&nbsp;LS7 2QT</span>
  </div>
  <div class="contact-divider"></div>
  <div class="contact contact-phone">
    <svg width="31" height="31" viewBox="0 0 30 30" aria-hidden="true"><circle cx="15" cy="15" r="15" fill="#fff"/><path d="M10.5 7.5l3 3.2-1.8 2.2c.9 2 2.5 3.6 4.5 4.5l2.2-1.8 3.2 3-1.6 2.8c-5.5-.4-11.2-6.1-11.6-11.6z" fill="#5f2589"/></svg>
    <span>&nbsp;0113 496 0732</span>
  </div>

  <div class="web-pill">www.pelinthaimassage.co.uk</div>
</main>
</body>
</html>
```